Varnel Group Business Card design with current logo

hello all , we have abranded logo which i will attach but we need a card double sided designed . one side is easy as its the logo but the other side we want clean and modern. The info needed will be the same text as the card sample attached. no pictures of us though just clean and professinal pls. Logo can be incorporated on the text side to for recognition. Colors are Black , white , red and grey... ideal card would be matt finish high end stock. or a black card so white text ... Sorry i have uploaded al the files i got when I had the logo designed on here.. Oh forgot want to say pls add in the card details EST 1981 and over 40yrs combined experiance
Updates

Hello everyone , I'm really sorry we haven't been able to make a final decision.. There is at least 3 cards that all have there positives over the other two... We will decide by tonight.

Target Market(s)

20-70 wide range but people with money and a education.

Industry/Entity Type

Real Estate Agent

Contact Information for Business Card

One side the Logo choose from the different color logos, black being the one we like most, other side is the details. Clean professional looking fonts. EST 1981 , over 40yrs experiance. Website email and both names and PH# as per the sample card attached

Font styles to use
Other font styles liked:
• Fonts:Code Bold,Code Light, Lucida Fax.

Colors
1b1b1b
757575
c9c9c9
e8e8e8
ffffff
e9e9e9

Requirements
Must have
• Logo and contact info

```html
<!DOCTYPE html>
<html lang="en">
<head>
<meta charset="utf-8">
<title>Varnel Group – Business Card</title>
<link rel="stylesheet" href="https://fonts.googleapis.com/css2?family=Open+Sans:wght@400;600&display=swap">
<style>
  :root {
    --backdrop: #2a2a2a;
    --card: #1b1b1b;
    --card-deep: #121212;
    --card-edge: #2b2b2b;
    --white: #ffffff;
    --light-grey: #c9c9c9;
    --grey: #757575;
    --accent: #c1272d;
  }
  * { margin: 0; padding: 0; box-sizing: border-box; }
  html, body {
    width: 1200px; height: 900px; overflow: hidden;
    background: var(--backdrop);
    font-family: "Open Sans", Arial, sans-serif;
  }
  .stage { position: relative; width: 1200px; height: 900px; }

  .card {
    position: absolute; left: 250px;
    width: 700px; height: 400px;
    background: linear-gradient(135deg, var(--card) 0%, var(--card-deep) 60%, var(--card-edge) 100%);
    box-shadow: 0 12px 30px rgba(0,0,0,.55);
    overflow: hidden;
  }
  .card--front { top: 30px; }
  .card--back { top: 470px; }

  .brand { position: absolute; display: flex; align-items: center; }
  .brand__square { background: var(--white); display: block; flex: none; }
  .brand__name {
    color: var(--white); font-weight: 400; letter-spacing: .08em;
    text-transform: uppercase; white-space: nowrap;
  }

  .card--front .brand { left: 70px; top: 100px; gap: 22px; }
  .card--front .brand__square { width: 110px; height: 110px; }
  .card--front .brand__name { font-size: 50px; }

  .front__dashes {
    position: absolute; left: 0; right: 0; top: 280px; height: 3px;
    background: repeating-linear-gradient(90deg, var(--accent) 0 40px, transparent 40px 62px);
  }

  .card--back .brand { left: 45px; top: 35px; gap: 14px; }
  .card--back .brand__square { width: 70px; height: 70px; }
  .card--back .brand__name { font-size: 32px; }

  .person { position: absolute; left: 45px; top: 135px; }
  .person__name { color: var(--white); font-size: 28px; font-weight: 600; line-height: 1.15; }
  .person__title { color: var(--light-grey); font-size: 17px; line-height: 1.3; }

  .back__rule {
    position: absolute; left: 240px; right: 0; top: 168px; height: 3px;
    background: var(--accent);
  }

  .contacts { position: absolute; left: 45px; top: 220px; list-style: none; }
  .contacts__item {
    display: flex; align-items: center; gap: 14px;
    color: var(--light-grey); font-size: 18px; height: 34px;
  }
  .contacts__icon {
    width: 24px; height: 24px; border-radius: 50%; flex: none;
    background: var(--accent); display: flex; align-items: center; justify-content: center;
    color: var(--white); font-size: 14px; font-weight: 600;
  }
  .contacts__icon svg { width: 14px; height: 14px; fill: var(--white); }

  .website {
    position: absolute; right: 40px; top: 188px;
    color: var(--light-grey); font-size: 17px;
  }
  .credentials {
    position: absolute; right: 40px; bottom: 34px; text-align: right;
  }
  .credentials__est {
    color: var(--white); font-size: 15px; font-weight: 600; letter-spacing: .15em;
  }
  .credentials__experience { color: var(--grey); font-size: 14px; margin-top: 2px; }
</style>
</head>
<body>
<main class="stage">

  <section class="card card--front" aria-label="Card front">
    <div class="brand">
      <span class="brand__square"></span>
      <span class="brand__name">Varnel Group</span>
    </div>
    <div class="front__dashes"></div>
  </section>

  <section class="card card--back" aria-label="Card back">
    <div class="brand">
      <span class="brand__square"></span>
      <span class="brand__name">Varnel Group</span>
    </div>

    <div class="person">
      <p class="person__name">Dorian Pell</p>
      <p class="person__title">Managing Director</p>
    </div>
    <div class="back__rule"></div>

    <ul class="contacts">
      <li class="contacts__item">
        <span class="contacts__icon">
          <svg viewBox="0 0 14 14"><rect x="3.5" y="0.5" width="7" height="13" rx="1.2"/><rect x="4.7" y="2" width="4.6" height="8" fill="#c1272d"/></svg>
        </span>0412 555 904
      </li>
      <li class="contacts__item">
        <span class="contacts__icon">
          <svg viewBox="0 0 14 14"><path d="M1 5c0-2 2-3 6-3s6 1 6 3v1h-3V4.5H4V6H1z"/><rect x="3" y="7" width="8" height="5" rx="1"/></svg>
        </span>90000418
      </li>
      <li class="contacts__item">
        <span class="contacts__icon">
          <svg viewBox="0 0 14 14"><path d="M7 0.5a4.5 4.5 0 0 0-4.5 4.5C2.5 8.5 7 13.5 7 13.5S11.5 8.5 11.5 5A4.5 4.5 0 0 0 7 .5zm0 6.3A1.8 1.8 0 1 1 7 3.2a1.8 1.8 0 0 1 0 3.6z"/></svg>
        </span>Harlow St 14, Sydney
      </li>
      <li class="contacts__item">
        <span class="contacts__icon">@</span>hello@varnelmail.com
      </li>
    </ul>

    <p class="website">www.varnelgroup.com</p>

    <div class="credentials">
      <p class="credentials__est">EST 1981</p>
      <p class="credentials__experience">Over 40 yrs combined experience</p>
    </div>
  </section>

</main>
</body>
</html>
```